Singapore Restaurant Menu Design

We need a menu designed for our new Singapore inspire restaurant located here in New Plymouth New Zealand. More Information in attached documents.
Updates

Sick

Target Market(s)

New Zealanders

Colors

Designer to choose only greyscale colors for use in the design.

Requirements
Nice to have
• Images of Singapore food however we do not want this to distract from the overall menu design as we still want the menu to be super clean

```html
<!DOCTYPE html>
<html lang="en">
<head>
<meta charset="utf-8">
<title>Singapore Restaurant Menu</title>
<link rel="stylesheet" href="https://fonts.googleapis.com/css2?family=Barlow+Condensed:wght@600;700&family=Josefin+Sans:wght@300&family=Crimson+Text:ital@1&display=swap">
<style>
  :root {
    --backdrop: #dadadc;
    --page-light: #f1eff2;
    --page-grey: #b3afb5;
    --ink-soft: #2f3f3b;
    --ink-soft-desc: #5b6663;
    --ink-dark: #141414;
    --ink-dark-desc: #2c2a2e;
    --leaf-deep: #3d6b3a;
    --leaf-mid: #7fae6a;
    --leaf-pale: #c9dcc0;
  }
  * { box-sizing: border-box; margin: 0; padding: 0; }
  html, body { width: 1200px; height: 840px; overflow: hidden; }
  body { background: var(--backdrop); position: relative; font-family: "Crimson Text", Georgia, serif; }

  .menu-spread {
    position: absolute; left: 34px; top: 20px;
    width: 1132px; height: 800px;
    display: flex;
    box-shadow: 0 10px 30px rgba(0,0,0,.18);
  }
  .page { position: relative; width: 566px; height: 800px; overflow: hidden; }
  .page--starters { background: var(--page-light); color: var(--ink-soft); }
  .page--mains { background: var(--page-grey); color: var(--ink-dark); }

  .foliage { position: absolute; }
  .foliage--top-left { left: 0; top: 0; width: 566px; height: 34px;
    background: linear-gradient(90deg, var(--leaf-mid), var(--leaf-pale) 40%, var(--leaf-mid) 75%, var(--leaf-pale)); }
  .foliage--corner-left { right: 0; top: 34px; width: 190px; height: 110px;
    background: linear-gradient(200deg, var(--leaf-mid), var(--leaf-pale) 60%, transparent); }
  .foliage--bottom-left { left: 0; bottom: 0; width: 566px; height: 30px;
    background: linear-gradient(90deg, var(--leaf-pale), var(--leaf-mid) 50%, var(--leaf-pale)); }
  .foliage--top-right { left: 0; top: 0; width: 566px; height: 40px;
    background: linear-gradient(90deg, var(--leaf-deep), var(--leaf-mid) 45%, var(--leaf-deep) 80%, var(--leaf-mid)); }
  .foliage--corner-right { right: 0; bottom: 0; width: 230px; height: 130px;
    background: linear-gradient(330deg, var(--leaf-deep), var(--leaf-mid) 55%, transparent); }
  .foliage--frond { left: 420px; top: 190px; width: 270px; height: 520px;
    background: radial-gradient(ellipse at 50% 50%, rgba(85,140,70,.75), rgba(85,140,70,.25) 55%, transparent 72%); }

  .section { position: absolute; }
  .section--starters { left: 48px; top: 70px; width: 330px; }
  .section--roti { left: 48px; top: 64px; width: 470px; }
  .section--noodle { left: 48px; top: 370px; width: 470px; }

  .section-title {
    display: inline-block;
    font-family: "Josefin Sans", sans-serif; font-weight: 300;
    font-size: 19px; letter-spacing: 3px; text-transform: uppercase;
    border: 1.5px solid currentColor; padding: 5px 10px 2px;
    margin-bottom: 12px;
  }
  .menu-item { display: grid; grid-template-columns: 1fr 44px; column-gap: 10px; margin-bottom: 12px; }
  .item-name {
    font-family: "Barlow Condensed", sans-serif; font-weight: 700;
    font-size: 13px; letter-spacing: 1.6px; text-transform: uppercase;
  }
  .item-price {
    font-family: "Barlow Condensed", sans-serif; font-weight: 700;
    font-size: 13px; letter-spacing: 1px; text-align: right; grid-row: span 2;
  }
  .item-desc { font-style: italic; font-size: 11.5px; line-height: 1.3; }
  .page--starters .item-desc { color: var(--ink-soft-desc); }
  .page--mains .item-desc { color: var(--ink-dark-desc); }
  .section--starters .menu-item { margin-bottom: 14px; grid-template-columns: 1fr 40px; width: 380px; }
</style>
</head>
<body>
<main class="menu-spread">
  <section class="page page--starters">
    <div class="foliage foliage--top-left" role="img" aria-label="Tropical green leaves along the top edge"></div>
    <div class="foliage foliage--corner-left" role="img" aria-label="Cluster of green leaves in the upper corner"></div>
    <div class="foliage foliage--bottom-left" role="img" aria-label="Green leaves along the bottom edge"></div>

    <div class="section section--starters">
      <h2 class="section-title">Starters</h2>
      <div class="menu-item"><span class="item-name">Bagedil (Potato Patties) (3 Pieces)</span><span class="item-price">$3</span>
        <p class="item-desc">Fried mashed potato patties with fresh cilantro, spring onions &amp; spices coated in flour and egg.</p></div>
      <div class="menu-item"><span class="item-name">Tahu Telor (Tofu with Egg)</span><span class="item-price">$10</span>
        <p class="item-desc">Fried spiced flour coated tofu drenched in egg, topped with satay sauce, crushed nuts &amp; fresh sprouts.</p></div>
      <div class="menu-item"><span class="item-name">Epok Epok (Curry Puffs) (3 Pieces)</span><span class="item-price">$5</span>
        <p class="item-desc">Malay style empanadas stuffed with choice of chicken curry, fork tender beef or curried potatoes &amp; seasonal veggies.</p></div>
      <div class="menu-item"><span class="item-name">Pakora</span><span class="item-price">$5</span>
        <p class="item-desc">Chickpea, red onion and potato fritters in a mildly spiced besan (chickpea flour) batter accompanied by a sweet tangy tamarind dip.</p></div>
      <div class="menu-item"><span class="item-name">Chana Vada (3 Pieces)</span><span class="item-price">$5</span>
        <p class="item-desc">Crunchy lentil fritters with onions, spices &amp; curry leaf.</p></div>
      <div class="menu-item"><span class="item-name">Fried Wonton (8 Pieces)</span><span class="item-price">$10</span>
        <p class="item-desc">Stuffed with choice of marinated spiced chicken / pork / pickled veggies with sweet soy dip.</p></div>
      <div class="menu-item"><span class="item-name">Gado Gado Salad</span><span class="item-price">$12</span>
        <p class="item-desc">A delicate salad of thinly sliced chinese cabbage, cucumber, beansprout, potatoes, french beans tossed in peanut dressing with boiled egg &amp; marinated prawns.</p></div>
      <div class="menu-item"><span class="item-name">Satay (6 Sticks)</span><span class="item-price">$12</span>
        <p class="item-desc">Grilled aromatic chicken / beef or tempeh (soy beans) on skewers accompanied by ketupat (rice cakes), cucumber, onions &amp; Singapore satay gravy.</p></div>
      <div class="menu-item"><span class="item-name">BBQ Chicken Wings (5 Pieces)</span><span class="item-price">$15</span>
        <p class="item-desc">Singapore style soy marinated BBQ chicken wings made to order with sweet chili dip.</p></div>
      <div class="menu-item"><span class="item-name">Fried Carrot Cake</span><span class="item-price">$10</span>
        <p class="item-desc">Savoury steamed white radish cake stir-fry with prawns &amp; egg drizzled with sweet dark soy sauce.</p></div>
    </div>
  </section>

  <section class="page page--mains">
    <div class="foliage foliage--top-right" role="img" aria-label="Dark green tropical leaves along the top edge"></div>
    <div class="foliage foliage--corner-right" role="img" aria-label="Green leaves in the lower corner"></div>

    <div class="section section--roti">
      <h2 class="section-title">Roti</h2>
      <div class="menu-item"><span class="item-name">Roti John – Made Famous in Kampong Serai</span><span class="item-price">$12</span>
        <p class="item-desc">Baguette loaf grilled with a topping choice of curried chicken / spiced beef or seasonal veggies cooked with egg and drizzled with chili sauce.</p></div>
      <div class="menu-item"><span class="item-name">Roti Prata (2 Pieces)</span><span class="item-price">$10</span>
        <p class="item-desc">A traditional crispy street food flat bread accompanied with choice of chicken or veg curry for dipping.</p></div>
      <div class="menu-item"><span class="item-name">Roti Jala (Malay Netted Crepe)</span><span class="item-price">$15</span>
        <p class="item-desc">Flour &amp; egg based batter spiced with tumeric and cumin accompanied with choice of chicken or veg curry.</p></div>
      <div class="menu-item"><span class="item-name">Murtabak (Stuffed Prata)</span><span class="item-price">$15</span>
        <p class="item-desc">Flour based crispy flat bread stuffed with choice of double cooked chicken curry, sauteed beef or seasonal veg curry.</p></div>
    </div>

    <div class="section section--noodle">
      <h2 class="section-title">Noodle</h2>
      <div class="menu-item"><span class="item-name">Wanton Mee</span><span class="item-price">$15</span>
        <p class="item-desc">Wonton noodles tossed in sweet dark soy sauce, sesame oil topped with pickled chili, cucumber &amp; broth with choice of bbq pork, chicken or prawns and fried crispy wontons.</p></div>
      <div class="menu-item"><span class="item-name">Seafood Mee Goreng</span><span class="item-price">$18</span>
        <p class="item-desc">Wok fried Malay style egg noodles in a homemade chili paste with prawns and squid topped with fried egg.</p></div>
      <div class="menu-item"><span class="item-name">Veggie Mee Goreng</span><span class="item-price">$15</span>
        <p class="item-desc">Wok fried Malay style egg noodles in homemade chili paste with seasonal veggies &amp; tofu.</p></div>
      <div class="menu-item"><span class="item-name">Char Kway Teow</span><span class="item-price">$15</span>
        <p class="item-desc">Wok fried rice cake strips in sweet dark soy sauce, fish oil, chili paste with seafood topped with beansprouts.</p></div>
      <div class="menu-item"><span class="item-name">Laksa Ala Katong Singapore</span><span class="item-price">$18</span>
        <p class="item-desc">A Peranakan style prawn based broth noodles with prawns, squid and mussels topped with boiled egg &amp; fried tofu cubes.</p></div>
      <div class="menu-item"><span class="item-name">Hor Fun Noodles</span><span class="item-price">$16</span>
        <p class="item-desc">Flat rice noodles stir fried with dark sweet soy sauce and a choice of seafood or pork in a silky egg gravy.</p></div>
    </div>
  </section>

  <div class="foliage foliage--frond" role="img" aria-label="Slender green palm frond crossing the centre fold"></div>
</main>
</body>
</html>
```